Infografiken für Unternehmensberatung zu Automatisierung und Digitalisierung
LRPT
Tolle Arbeit in kurzer Zeit fertigestellt. Zügige Kommunikation, Umsetzung und Anpassungen. Ich bin sehr zufrieden und kann Lady Corntwig mit einem gutem Gefühl weiterempfehlen. Danke
Zielgruppe
Unternehmensberatung zu Automatisierung und Digitalisierung
Aufgabenstellung
Hochwertiges und ansprechendes Design der Beratungsprozesse. Grafik soll in verschiedene Größen eingesetzt und farblich auf das CI der Website/Logos abgestimmt sein.
Gerne kann zwischen den drei Kreisen etwas Raum sein oder der äußere Kreis aus einzelnen Feldern bestehen. Die Beschriftung soll an den Kreisradius angepasst werden. Das copyright bitte auch an den Radius des Kreis anpassen.

```html
<!DOCTYPE html>
<html lang="de">
<head>
<meta charset="utf-8">
<title>Systemlösung – Brightpath Beratung KG</title>
<link href="https://fonts.googleapis.com/css2?family=Fira+Sans:wght@400;600;700&display=swap" rel="stylesheet">
<style>
  :root {
    --brand-blue: #22508f;
    --ring-grey: #c9c9c9;
    --core-blue: #9db6dc;
    --subtitle-grey: #c8c8c8;
    --paper: #ffffff;
    --ink: #111111;
  }
  html, body {
    margin: 0;
    padding: 0;
    width: 849px;
    height: 1200px;
    overflow: hidden;
    background: var(--paper);
  }
  .poster {
    display: block;
    width: 849px;
    height: 1200px;
    font-family: "Fira Sans", sans-serif;
  }
  .title {
    fill: var(--brand-blue);
    font-weight: 700;
    font-size: 64px;
    letter-spacing: 14px;
  }
  .subtitle {
    fill: var(--subtitle-grey);
    font-weight: 700;
    font-size: 40px;
  }
  .subtitle-rule { stroke: var(--subtitle-grey); stroke-width: 4; }
  .outer-disc { fill: var(--brand-blue); }
  .gap { fill: var(--paper); }
  .middle-ring { fill: var(--ring-grey); }
  .core { fill: var(--core-blue); }
  .divider { stroke: var(--paper); stroke-width: 10; }
  .notch { fill: var(--paper); }
  .step-label {
    fill: var(--paper);
    font-size: 36px;
    letter-spacing: 4px;
  }
  .pillar-label {
    fill: var(--ink);
    font-size: 34px;
    letter-spacing: 2px;
  }
  .core-label {
    fill: var(--paper);
    font-size: 37px;
    text-anchor: middle;
  }
  .copyright {
    fill: var(--ink);
    font-size: 18px;
    letter-spacing: 2px;
  }
</style>
</head>
<body>
<svg class="poster" viewBox="0 0 1240 1754" xmlns="http://www.w3.org/2000/svg" role="img" aria-label="Systemlösung: Kreisdiagramm der Beratungsprozesse">
  <defs>
    <!-- clockwise arcs centred at the top -->
    <path id="cw-412" d="M304.4 673.1 A412 412 0 0 1 935.6 673.1"/>
    <path id="cw-375" d="M332.7 696.9 A375 375 0 0 1 907.3 696.9"/>
    <path id="cw-395" d="M317.4 684 A395 395 0 0 1 922.6 684"/>
    <path id="cw-190" d="M474.5 815.8 A190 190 0 0 1 765.5 815.8"/>
    <path id="cw-150" d="M505.1 841.5 A150 150 0 0 1 734.9 841.5"/>
    <!-- counter-clockwise arcs centred at the bottom -->
    <path id="ccw-390" d="M321.3 1188.8 A390 390 0 0 0 918.7 1188.8"/>
    <path id="ccw-428" d="M292.2 1213.2 A428 428 0 0 0 947.8 1213.2"/>
    <path id="ccw-175" d="M486 1050.5 A175 175 0 0 0 754 1050.5"/>
    <path id="ccw-215" d="M455.3 1076.2 A215 215 0 0 0 784.7 1076.2"/>
    <path id="ccw-555" d="M194.9 1294.9 A555 555 0 0 0 1045.1 1294.9"/>
  </defs>

  <!-- header -->
  <text class="title" x="620" y="185" text-anchor="middle">SYSTEMLÖSUNG</text>
  <line class="subtitle-rule" x1="302" y1="216" x2="364" y2="216"/>
  <line class="subtitle-rule" x1="876" y1="216" x2="924" y2="216"/>
  <text class="subtitle" x="374" y="230" textLength="494" lengthAdjust="spacingAndGlyphs">Brightpath Beratung KG</text>

  <!-- outer process ring -->
  <circle class="outer-disc" cx="620" cy="938" r="535"/>
  <circle class="gap" cx="620" cy="938" r="302"/>
  <g class="outer-dividers">
    <line class="divider" x1="620" y1="638" x2="620" y2="393"/>
    <line class="divider" x1="879.8" y1="788" x2="1092" y2="665.5"/>
    <line class="divider" x1="879.8" y1="1088" x2="1092" y2="1210.5"/>
    <line class="divider" x1="620" y1="1238" x2="620" y2="1483"/>
    <line class="divider" x1="360.2" y1="1088" x2="148" y2="1210.5"/>
    <line class="divider" x1="360.2" y1="788" x2="148" y2="665.5"/>
  </g>
  <g class="notches">
    <polygon class="notch" points="620,588 620,438 685,513"/>
    <polygon class="notch" points="923.1,763 1053,688 1020.6,781.8"/>
    <polygon class="notch" points="923.1,1113 1053,1188 955.6,1206.8"/>
    <polygon class="notch" points="620,1288 620,1438 555,1363"/>
    <polygon class="notch" points="316.9,1113 187,1188 219.4,1094.2"/>
    <polygon class="notch" points="316.9,763 187,688 284.4,669.2"/>
  </g>

  <!-- middle pillar ring -->
  <circle class="middle-ring" cx="620" cy="938" r="288"/>
  <circle class="gap" cx="620" cy="938" r="133"/>
  <g class="pillar-dividers">
    <line class="divider" x1="730.9" y1="874" x2="872.9" y2="792"/>
    <line class="divider" x1="620" y1="1066" x2="620" y2="1230"/>
    <line class="divider" x1="509.1" y1="874" x2="367.1" y2="792"/>
  </g>

  <!-- core -->
  <circle class="core" cx="620" cy="938" r="118"/>
  <text class="core-label" x="620" y="903">Zeit &amp;</text>
  <text class="core-label" x="620" y="947">Lebens-</text>
  <text class="core-label" x="620" y="991">qualität</text>

  <!-- outer step labels -->
  <g transform="rotate(30 620 938)">
    <text class="step-label" text-anchor="middle"><textPath href="#cw-395" startOffset="50%">Strategie</textPath></text>
  </g>
  <g transform="rotate(90 620 938)">
    <text class="step-label" text-anchor="middle"><textPath href="#cw-412" startOffset="50%">Eindeutige</textPath></text>
    <text class="step-label" text-anchor="middle"><textPath href="#cw-375" startOffset="50%">Zielgruppe</textPath></text>
  </g>
  <g transform="rotate(-30 620 938)">
    <text class="step-label" text-anchor="middle"><textPath href="#ccw-390" startOffset="50%">Systematisch</textPath></text>
    <text class="step-label" text-anchor="middle"><textPath href="#ccw-428" startOffset="50%">informieren</textPath></text>
  </g>
  <g transform="rotate(30 620 938)">
    <text class="step-label" text-anchor="middle"><textPath href="#ccw-390" startOffset="50%">Magnet-</textPath></text>
    <text class="step-label" text-anchor="middle"><textPath href="#ccw-428" startOffset="50%">Marketing</textPath></text>
  </g>
  <g transform="rotate(-90 620 938)">
    <text class="step-label" text-anchor="middle"><textPath href="#cw-412" startOffset="50%">Verkaufen</textPath></text>
    <text class="step-label" text-anchor="middle"><textPath href="#cw-375" startOffset="50%">&amp; betrachten</textPath></text>
  </g>
  <g transform="rotate(-30 620 938)">
    <text class="step-label" text-anchor="middle"><textPath href="#cw-412" startOffset="50%">Team bilden</textPath></text>
    <text class="step-label" text-anchor="middle"><textPath href="#cw-375" startOffset="50%">&amp; entwicklen</textPath></text>
  </g>

  <!-- pillar labels -->
  <text class="pillar-label" text-anchor="middle"><textPath href="#cw-190" startOffset="50%">Automatisieren</textPath></text>
  <text class="pillar-label" text-anchor="middle"><textPath href="#cw-150" startOffset="50%">&amp; Digitalisieren</textPath></text>
  <g transform="rotate(-60 620 938)">
    <text class="pillar-label" text-anchor="middle"><textPath href="#ccw-175" startOffset="50%">Unternehmen</textPath></text>
    <text class="pillar-label" text-anchor="middle"><textPath href="#ccw-215" startOffset="50%">skalieren</textPath></text>
  </g>
  <g transform="rotate(60 620 938)">
    <text class="pillar-label" text-anchor="middle"><textPath href="#ccw-175" startOffset="50%">Expteren</textPath></text>
    <text class="pillar-label" text-anchor="middle"><textPath href="#ccw-215" startOffset="50%">Positionierung</textPath></text>
  </g>

  <!-- copyright along the circle -->
  <text class="copyright" text-anchor="middle"><textPath href="#ccw-555" startOffset="50%">Copyright© Brightpath Beratung KG | www.brightpath-beratung.de</textPath></text>
</svg>
</body>
</html>
```